Attorney Website Design

I need a top quality attorney website layout designed. Here are some examples of what I feel are great websites:
http://www.brelmoradivorceattorney.example/
http://www.vethomirlawfirm.example/
http://www.plexfirm.example/
http://www.harrowgatecriminaldefensefirm.example/
http://www.qzfirm.example/
http://www.tolvermoorcriminaldefensefirm.example/
http://www.drennocriminalattorneys.example/
http://www.qzfirm.example/
What we like about these sites:
• The different layers
• Subtle designs, textures, curves
• 3 dimensional
• Floating effects
• Prominent phone number
• Location of Areas of Practice
• Request A Consultation Prominent
• Right side bar with practice areas
• Badges
• Clear Calls to Action
• Dynamic/Staying Top navigation when you scroll
The project will be for a home page and then also an interior page (should be similar to home page).
I want to make it understood I am looking for a design which is not a typical "template" site which I can find anywhere for $50. This budget and project is for a "Custom" website design. Please submit designs similar in quality to the samples links I have posted. Creativity is a MUST! The best way to explain this is, I want a design that I can feel it unique and original, not something that looks like 95% of all websites out there.
Owen
I just wanted everyone to know that so far I am not to pleased with any of the designs. I am not looking for cut/pasting of other peoples websites but ORIGINAL and CREATIVE work.
Industry/Entity Type
Attorney

```html
<!DOCTYPE html>
<html lang="en">
<head>
<meta charset="utf-8">
<title>Attorneys You Can Trust</title>
<link rel="stylesheet" href="https://fonts.googleapis.com/css2?family=Bebas+Neue&family=Lobster&family=Open+Sans:wght@400&family=Limelight&display=swap">
<style>
  :root {
    --bar-brown: #5a4d4c;
    --bar-edge: #d9b98a;
    --tan: #c9a479;
    --shield-face: #e6eaec;
    --shield-rim: #4a4444;
    --ink: #111111;
    --white: #ffffff;
    --court-warm: #9a6a3c;
    --court-dark: #3b2718;
    --grey-dark: #5c5c5c;
    --grey-light: #e4e4e4;
  }
  * { margin: 0; padding: 0; box-sizing: border-box; }
  html, body { width: 1200px; height: 1000px; overflow: hidden; }
  body { position: relative; font-family: "Open Sans", sans-serif; background: var(--court-dark); }

  .hero-backdrop {
    position: absolute; inset: 0;
    background:
      radial-gradient(ellipse at 55% 25%, #c8915a 0%, transparent 55%),
      radial-gradient(ellipse at 90% 40%, #9d8a55 0%, transparent 40%),
      linear-gradient(180deg, #7a4b2a 0%, var(--court-warm) 35%, #6a3a20 70%, var(--court-dark) 100%);
  }

  .facet { position: absolute; inset: 0; width: 1200px; height: 1000px; }

  .team-photo {
    position: absolute; left: 295px; top: 490px; width: 610px; height: 510px;
    background: radial-gradient(ellipse at 55% 60%, #2a2320 0%, #3d2e25 45%, rgba(80,55,40,0.5) 75%, transparent 100%);
  }

  .main-nav { position: absolute; inset: 0; width: 1200px; height: 340px; }
  .nav-link {
    position: absolute; font-family: "Lobster", cursive; font-size: 29px;
    color: var(--white); text-decoration: none; text-shadow: 1px 2px 2px rgba(0,0,0,0.6);
  }
  .nav-link.is-active { color: var(--white); }

  .brand-name {
    position: absolute; left: 455px; top: 52px; width: 293px; text-align: center;
    font-family: "Limelight", serif; font-size: 58px; color: #2b2323; letter-spacing: -1px;
  }
  .call-box {
    position: absolute; left: 510px; top: 168px; width: 185px; text-align: center; color: var(--white);
  }
  .call-box .call-label { font-size: 14px; line-height: 20px; }
  .call-box .call-number { font-size: 23px; line-height: 32px; }

  .headline {
    position: absolute; left: 0; width: 1200px; text-align: center;
    font-family: "Bebas Neue", sans-serif; font-size: 62px; line-height: 1;
  }
  .headline.line-one { top: 322px; color: var(--white); }
  .headline.line-two { top: 398px; color: var(--ink); }
  .tagline {
    position: absolute; top: 457px; left: 0; width: 1200px; text-align: center;
    font-size: 17px; color: #2a1c14;
  }
  .tagline-rule { position: absolute; top: 469px; height: 1px; width: 30px; background: rgba(255,255,255,0.45); }

  .consult-title {
    position: absolute; left: 1099px; top: 814px; white-space: nowrap;
    font-family: "Bebas Neue", sans-serif; font-size: 30px; color: var(--ink);
  }
  .consult-field {
    position: absolute; left: 1088px; width: 200px; height: 43px;
    background: var(--white); border: 1px solid #cfcfcf; border-radius: 5px;
    padding-left: 16px; font-size: 17px; line-height: 41px; color: #9a9a9a; white-space: nowrap;
  }
</style>
</head>
<body>
  <div class="hero-backdrop" role="img" aria-label="Blurred courtroom interior with wooden benches and scales of justice"></div>

  <svg class="facet" viewBox="0 0 1200 1000" aria-hidden="true">
    <defs>
      <linearGradient id="facetLeft" x1="0" y1="0" x2="1" y2="1">
        <stop offset="0" stop-color="#8a8a8a"/><stop offset="1" stop-color="#3f3f3f"/>
      </linearGradient>
      <linearGradient id="facetRight" x1="0" y1="0" x2="1" y2="1">
        <stop offset="0" stop-color="#bdbdbd"/><stop offset="1" stop-color="#f0f0f0"/>
      </linearGradient>
    </defs>
    <polygon points="0,570 430,1000 0,1000" fill="url(#facetLeft)"/>
    <polygon points="1200,572 776,1000 1200,1000" fill="url(#facetRight)"/>
  </svg>

  <div class="team-photo" role="img" aria-label="Attorney in pinstripe suit holding a leather folder, with three colleagues seated at a table behind him"></div>

  <svg class="facet" viewBox="0 0 1200 1000" aria-hidden="true">
    <polygon points="505,1000 603,903 701,1000" fill="var(--white)"/>
  </svg>

  <nav class="main-nav">
    <svg width="1200" height="340" viewBox="0 0 1200 340" aria-hidden="true" style="position:absolute;inset:0">
      <defs>
        <linearGradient id="edgeGold" x1="0" y1="0" x2="0" y2="1">
          <stop offset="0" stop-color="#f0d6a8"/><stop offset="1" stop-color="#b08a5c"/>
        </linearGradient>
        <linearGradient id="pill" x1="0" y1="0" x2="0" y2="1">
          <stop offset="0" stop-color="#e2c092"/><stop offset="1" stop-color="#a98156"/>
        </linearGradient>
      </defs>
      <polygon points="78,85 470,100 470,178 78,196 50,132" fill="url(#edgeGold)"/>
      <polygon points="80,90 468,104 468,174 80,190" fill="var(--bar-brown)"/>
      <polygon points="1128,85 735,100 735,178 1128,196 1156,132" fill="url(#edgeGold)"/>
      <polygon points="1126,90 737,104 737,174 1126,190" fill="var(--bar-brown)"/>
      <polygon points="204,112 330,112 341,135 330,158 204,158 192,135" fill="url(#pill)"/>
      <path d="M462,60 Q600,-10 742,60 L745,160 Q720,250 602,317 Q484,250 458,160 Z" fill="var(--shield-rim)"/>
      <path d="M470,68 Q600,5 734,68 L736,160 Q712,240 602,302 Q492,240 468,160 Z" fill="var(--shield-face)"/>
      <path d="M523,146 L683,146 L694,158 L694,238 L683,250 L523,250 L511,238 L511,158 Z" fill="#000" stroke="#cfcfcf" stroke-width="1.5"/>
      <path d="M518,153 L688,153 L688,243 L518,243 Z" fill="none" stroke="#888" stroke-width="1"/>
      <line x1="555" y1="160" x2="648" y2="160" stroke="#ddd" stroke-width="1"/>
      <line x1="560" y1="235" x2="648" y2="235" stroke="#ddd" stroke-width="1"/>
    </svg>
    <a class="nav-link" href="#" style="left:102px;top:112px">Home</a>
    <a class="nav-link is-active" href="#" style="left:216px;top:112px">Projects</a>
    <a class="nav-link" href="#" style="left:359px;top:112px">About</a>
    <div class="brand-name">LOGO</div>
    <div class="call-box">
      <div class="call-label">Call</div>
      <div class="call-number">555.014.2938</div>
    </div>
    <a class="nav-link" href="#" style="left:768px;top:112px">Portfolio</a>
    <a class="nav-link" href="#" style="left:911px;top:112px">Blog</a>
    <a class="nav-link" href="#" style="left:1009px;top:112px">Contact</a>
  </nav>

  <h1 class="headline line-one">Attorneys You</h1>
  <h2 class="headline line-two">Can Trust</h2>
  <span class="tagline-rule" style="left:416px"></span>
  <p class="tagline">We are a team of professionals</p>
  <span class="tagline-rule" style="left:760px"></span>

  <section class="consult-form">
    <h3 class="consult-title">Request A Consultation</h3>
    <div class="consult-field" style="top:889px">Your Name</div>
    <div class="consult-field" style="top:955px">Phone Number</div>
  </section>
</body>
</html>
```